Cyber Security Site Design (Products & Consulting)

I need my website redesigned to be engaging, clean, efficient and modern. My company (when its up and running) is going to be concentrated on two things: a few specific products for cyber security as well as cyber security consulting services. The background I bring to the field is having worked with small companies all the way to the largest government organizations and advising them on their security posture and how to improve it. We need the ability to add products and services easily.

For a sample product, you can use either Tarnel (http://www.tarnel-relay.org/) or Vornidex Graywell (https://www.vornidex.com/products/relay-kx-and-enhanced-safe-portal).

It will replace https://dalmorenvue.com/

Target Market(s)

Cyber Security professionals in all verticals

Coding

Coded - Design and coding required

Number of Pages Required

4 page

Font styles to use
Sans Serif

Colors
6b449b

Requirements
Must have
• Ability to easily modify
• Have main page
• Have product specific pages
• Have consulting services pages
• Have executive team information
• Clean, modern design
• Usage of the logo and its color scheme
Nice to have
• I like the idea of a left collapsed sidebar (so icons only) that can expand for text.
• I am also open to a very unique landing page, possibly a shape in the middle (hexagons maybe?) with each of the options there.
Should not have
• Nothing that looks like it came out of a hacker movie

```html
<!DOCTYPE html>
<html lang="en">
<head>
<meta charset="utf-8">
<title>Dalmoren Vue — Services</title>
<link rel="stylesheet" href="https://fonts.googleapis.com/css2?family=Exo+2:wght@400;500;700&family=Roboto:wght@400;500&family=Montserrat:wght@400&display=swap">
<style>
:root{
  --brand:#6b449b;
  --brand-deep:#62389a;
  --brand-dark:#4e2a7a;
  --ink:#1f1f24;
  --muted:#3a3a42;
  --card:#f3f3f3;
  --line:#dddddd;
  --white:#ffffff;
}
*{box-sizing:border-box;margin:0;padding:0}
html,body{width:681px;height:1200px;overflow:hidden;background:var(--white)}
.page{position:relative;width:681px;height:1200px;overflow:hidden;font-family:"Roboto",sans-serif;color:var(--ink)}
.abs{position:absolute}

/* header */
.brand{position:absolute;display:flex;align-items:center;gap:5px;font-family:"Exo 2",sans-serif;font-weight:500}
.brand .dot{width:12px;height:12px;border-radius:50%;background:var(--brand)}
.header .brand{left:80px;top:10px;font-size:17px;color:var(--brand)}
.nav a{position:absolute;top:15px;font-size:7.4px;color:var(--ink);text-decoration:none;letter-spacing:.1px}
.nav a.active{color:var(--brand)}
.pill{position:absolute;display:flex;align-items:center;gap:5px;background:var(--brand);color:var(--white);border-radius:12px;font-size:7.2px;font-weight:500;padding-left:6px;box-shadow:0 2px 4px rgba(107,68,155,.35)}
.pill i{width:10px;height:10px;border-radius:50%;border:1.5px solid var(--white)}

/* hero */
.hero{position:absolute;left:0;top:40px;width:681px;height:212px;clip-path:polygon(0 0,100% 0,100% 145px,340px 212px,0 145px);
  background:linear-gradient(180deg,#6f7f9a 0%,#8a8a94 30%,#9d7a66 55%,#6d5147 80%,#4a3a35 100%)}
.hero-title{position:absolute;left:0;width:681px;top:106px;text-align:center;font-family:"Exo 2",sans-serif;font-weight:700;font-size:25px;color:var(--white);text-shadow:0 1px 3px rgba(0,0,0,.35)}
.hero-sub{position:absolute;left:0;width:681px;top:138px;text-align:center;font-family:"Exo 2",sans-serif;font-size:10px;color:var(--white);text-shadow:0 1px 2px rgba(0,0,0,.4)}

.crumb{position:absolute;left:80px;top:244px;font-size:7.4px}
.crumb span{color:var(--brand);margin-left:6px}

/* services */
.section-title{position:absolute;left:0;width:681px;top:290px;text-align:center;font-family:"Exo 2",sans-serif;font-size:23px;font-weight:400;color:var(--ink)}
.section-title b{font-weight:700}
.rule{position:absolute;left:265px;top:328px;width:152px;height:1px;background:var(--line)}
.rule-mark{position:absolute;left:329px;top:327px;width:24px;height:2px;background:var(--brand)}

.card{position:absolute;width:222px;height:146px;background:var(--card);text-align:center}
.card .icon{position:absolute;left:84px;top:12px;width:55px;height:55px;border-radius:50%;background:#e6e1ec;display:flex;align-items:center;justify-content:center}
.card .icon div{width:50px;height:50px;border-radius:50%;background:var(--brand);display:flex;align-items:center;justify-content:center}
.card h3{position:absolute;left:0;width:100%;top:76px;font-family:"Exo 2",sans-serif;font-weight:500;font-size:11.5px;color:var(--ink)}
.card p{position:absolute;left:18px;right:18px;top:96px;font-family:"Montserrat",sans-serif;font-size:7.2px;line-height:11.6px;color:var(--muted)}

/* footer */
.footer-band{position:absolute;left:0;top:862px;width:681px;height:310px;background:var(--brand-deep);clip-path:polygon(0 25px,341px 0,100% 25px,100% 100%,0 100%)}
.footer-band .sep{position:absolute;left:0;top:65px;width:681px;height:1px;background:rgba(255,255,255,.12)}
.footer .brand{left:0;width:681px;justify-content:center;top:888px;font-size:19px;color:var(--white)}
.footer .brand .dot{background:var(--white);width:14px;height:14px}
.ghost{position:absolute;left:285px;top:870px;width:110px;height:110px;border-radius:50%;background:rgba(255,255,255,.05)}

.cta-title{position:absolute;left:78px;top:952px;font-family:"Exo 2",sans-serif;font-size:20px;color:var(--white)}
.cta-title b{font-weight:700}
.cta-text{position:absolute;left:80px;top:981px;width:220px;font-size:8.2px;line-height:10px;color:var(--white)}

.col-title{position:absolute;font-family:"Exo 2",sans-serif;font-size:9.5px;font-weight:500;color:var(--white)}
.col-title::after{content:"";position:absolute;left:0;top:15px;width:25px;height:1px;background:rgba(255,255,255,.6)}
.contact{position:absolute;left:78px;color:var(--white);font-size:6.4px;line-height:10px}
.contact strong{font-size:7.2px;font-weight:500}
.contact.phone{font-size:9.5px;font-weight:500}
.contact svg{position:absolute;left:0;top:1px}
.contact .txt{padding-left:13px}
.links{position:absolute;left:227px;top:1052px;list-style:none;font-size:6.4px;line-height:11px;color:var(--white)}
.links li::before{content:"›";margin-right:6px}

.form{position:absolute;left:348px;top:953px;width:253px;height:219px;background:var(--white)}
.field{position:absolute;left:20px;width:212px;height:21.5px;border:1px solid #cfcfcf;font-family:"Montserrat",sans-serif;font-size:6.8px;color:#555;padding:7px 0 0 8px}
.field.msg{height:34px;padding-top:5px}

.bottom{position:absolute;left:0;top:1172px;width:681px;height:28px;background:var(--brand-dark)}
.copy{position:absolute;left:80px;top:10px;font-family:"Montserrat",sans-serif;font-size:6.4px;color:var(--white)}
.social{position:absolute;top:5px;width:16px;height:16px;border-radius:50%;border:1px solid rgba(255,255,255,.8)}
</style>
</head>
<body>
<div class="page">

  <header class="header">
    <div class="brand"><span class="dot"></span>Dalmoren Vue</div>
    <nav class="nav">
      <a style="left:258px">HOME</a>
      <a style="left:298px">ABOUT</a>
      <a style="left:342px">OUR TEAM</a>
      <a style="left:397px">OUR PRODUCTS</a>
      <a class="active" style="left:470px">SERVICES</a>
    </nav>
    <div class="pill" style="left:526px;top:11px;width:72px;height:18px"><i></i>CONTACT US</div>
  </header>

  <div class="hero" role="img" aria-label="Photo of a city skyline at dusk"></div>
  <h1 class="hero-title">CYBER SECURITY CONSULTING &amp; PRODUCTS</h1>
  <p class="hero-sub">A full range of Cyber Security Consulting Services and Products to meet your business requirements</p>
  <div class="pill" style="left:290px;top:167px;width:98px;height:19px"><i></i>GET STARTED NOW!</div>

  <div class="crumb">HOME <span style="color:var(--ink)">»</span><span>SERVICES</span></div>

  <h2 class="section-title">OUR <b>SERVICES</b></h2>
  <div class="rule"></div><div class="rule-mark"></div>

  <article class="card" style="left:110px;top:347px">
    <div class="icon"><div><svg width="28" height="22" viewBox="0 0 28 22" fill="none" stroke="#fff" stroke-width="1.3"><rect x="1" y="1" width="26" height="20" rx="1"/><line x1="1" y1="5" x2="27" y2="5"/><rect x="11" y="12" width="6" height="6"/><path d="M12 12v-2a2 2 0 0 1 4 0v2"/><line x1="4" y1="9" x2="10" y2="9"/><line x1="18" y1="9" x2="24" y2="9"/></svg></div></div>
    <h3>Cyber Security Services</h3>
    <p>Lorem ipsum dolor sit amet, consectetur adipiscing elit, sed do eiusmod tempor incididunt ut labore et dolore magna aliqua.</p>
  </article>
  <article class="card" style="left:348px;top:347px">
    <div class="icon"><div><svg width="22" height="28" viewBox="0 0 22 28" fill="none" stroke="#fff" stroke-width="1.3"><path d="M1 1h14l6 6v20H1z"/><circle cx="11" cy="12" r="4"/><line x1="4" y1="22" x2="18" y2="22"/></svg></div></div>
    <h3>Managed Security Services</h3>
    <p>Lorem ipsum dolor sit amet, consectetur adipiscing elit, sed do eiusmod tempor incididunt ut labore et dolore magna aliqua.</p>
  </article>
  <article class="card" style="left:110px;top:510px">
    <div class="icon"><div><svg width="28" height="28" viewBox="0 0 28 28" fill="none" stroke="#fff" stroke-width="1.3"><circle cx="14" cy="14" r="12"/><line x1="14" y1="2" x2="14" y2="26"/><circle cx="8" cy="10" r="2"/><circle cx="20" cy="18" r="2"/></svg></div></div>
    <h3>Deep Slight Intelligence</h3>
    <p>Lorem ipsum dolor sit amet, consectetur adipiscing elit, sed do eiusmod tempor incididunt ut labore et dolore magna aliqua.</p>
  </article>
  <article class="card" style="left:348px;top:510px">
    <div class="icon"><div><svg width="30" height="28" viewBox="0 0 30 28" fill="none" stroke="#fff" stroke-width="1.3"><line x1="15" y1="2" x2="15" y2="14"/><path d="M12 5l3-3 3 3"/><line x1="5" y1="8" x2="5" y2="20"/><line x1="25" y1="8" x2="25" y2="20"/><path d="M2 26h26"/><path d="M9 26a6 6 0 0 1 12 0"/></svg></div></div>
    <h3>Incident Response Services</h3>
    <p>Lorem ipsum dolor sit amet, consectetur adipiscing elit, sed do eiusmod tempor incididunt ut labore et dolore magna aliqua.</p>
  </article>
  <article class="card" style="left:110px;top:673px">
    <div class="icon"><div><svg width="26" height="26" viewBox="0 0 26 26" fill="none" stroke="#fff" stroke-width="1.4"><line x1="4" y1="22" x2="20" y2="6"/><circle cx="21" cy="5" r="3"/><line x1="6" y1="4" x2="22" y2="20"/><rect x="3" y="2" width="4" height="4"/></svg></div></div>
    <h3>Other Services</h3>
    <p>Lorem ipsum dolor sit amet, consectetur adipiscing elit, sed do eiusmod tempor incididunt ut labore et dolore magna aliqua.</p>
  </article>

  <footer class="footer">
    <div class="footer-band"><div class="sep"></div></div>
    <div class="ghost"></div>
    <div class="brand"><span class="dot"></span>Dalmoren Vue</div>

    <h2 class="cta-title"><b>LET’S</b> GET STARTED</h2>
    <p class="cta-text">Take the first step to growing your business with a FREE consultation and quote.</p>
    <svg class="abs" style="left:256px;top:960px" width="95" height="70" viewBox="0 0 95 70" fill="none" stroke="#fff" stroke-width=".8" stroke-dasharray="2 2"><path d="M2 6C30 0 45 8 42 22c-3 14-16 10-12 0 5-10 40-8 50 10 6 10 7 20 7 30"/></svg>

    <div class="col-title" style="left:78px;top:1030px">Contact Details</div>
    <div class="contact" style="top:1054px">
      <svg width="6" height="8" viewBox="0 0 6 8"><path d="M3 0a3 3 0 0 1 3 3c0 2-3 5-3 5S0 5 0 3a3 3 0 0 1 3-3z" fill="#fff"/><circle cx="3" cy="3" r="1" fill="#62389a"/></svg>
      <div class="txt"><strong>DALMOREN CYBER SECURITY</strong><br>4810 Harlow Crest Rd, Suite<br>#220 Millbrook, TX 77541.</div>
    </div>
    <div class="contact phone" style="top:1088px">
      <svg width="7" height="7" viewBox="0 0 7 7"><path d="M1 0l1.5 1.8-.8 1a4 4 0 0 0 1.5 1.5l1-.8L7 5.5 6 7C3 7 0 4 0 1z" fill="#fff"/></svg>
      <div class="txt">555-014-7290</div>
    </div>
    <div class="contact" style="top:1107px">
      <svg width="8" height="6" viewBox="0 0 8 6"><rect width="8" height="6" fill="#fff"/><path d="M0 0l4 3 4-3" stroke="#62389a" fill="none" stroke-width=".8"/></svg>
      <div class="txt">info@dalmorencyber.com</div>
    </div>

    <div class="col-title" style="left:227px;top:1029px">Quick Links</div>
    <ul class="links">
      <li>Home</li><li>About Us</li><li>Our Team</li><li>Our Products</li><li>Services</li><li>Conatact</li>
    </ul>

    <form class="form">
      <div class="field" style="top:22px">First Name</div>
      <div class="field" style="top:50px">Last Name</div>
      <div class="field" style="top:78px">Email</div>
      <div class="field" style="top:106px">Phone Number</div>
      <div class="field msg" style="top:134px">Message</div>
      <div class="pill" style="left:20px;top:182px;width:58px;height:18px"><i></i>SUBMIT</div>
    </form>

    <div class="bottom">
      <p class="copy">Copyright © 2018 <b>DalmorenCyberSecurity</b>. All Right Reserved.</p>
      <span class="social" style="left:443px"></span>
      <span class="social" style="left:463px"></span>
      <span class="social" style="left:484px"></span>
      <span class="social" style="left:504px"></span>
    </div>
  </footer>

</div>
</body>
</html>
```